Vinyl Apple Design of House Music Label

We need an apple vinyl record design of both sides (a round sticker in the middle of the vinyl record). We write minimal and house music. Like Tom Velk and Rupert Calloway. We would like to see the design in bright colors, with patterns and swirls. Also, for future releases, the design of each release will change slightly. Easily changeable designs - welcome. Sizes attached.

Requirements
Nice to have
• Everything is at the discretion of the designer, but here are some of the works that I liked-
• https://www.spinvault.example/Rupert_Calloway_Folded_TARN026_Vinyl__512907
• https://www.spinvault.example/Rupert_Calloway_Copper_Tide_EP_KELP032_Vinyl__648201
• https://www.spinvault.example/Rupert_Calloway_%26_Dorian_Pike_Brql_Ep_TARN021_Vinyl__731450
• https://www.spinvault.example/Valo_Strich_Amber_Yard_Tilt_EP_GWSN004_Vinyl__205813
• https://www.spinvault.example/Nathaniel_Brisco_Quiet_Prismata_Ep_DLV006_Vinyl__864027
• https://www.spinvault.example/Fern_Halo_Tender_EP_WSK001_Vinyl__317642
• https://www.spinvault.example/Plimo_Nebelzeit_GOR006_Vinyl__458219
• https://www.spinvault.example/Jed_Toro_Mirror_Fever_KQ12_Vinyl__690354
• https://www.spinvault.example/Wendra_Loop_Nine_EP_KQ15_Vinyl__183967
• The content of the text is allowed, but not required. - label name (Trelvin Records), 4 tracks (author and title), name of the distributor

```html
<!DOCTYPE html>
<html lang="en">
<head>
<meta charset="utf-8">
<title>Trelvin Records – Vinyl Labels, Side A and Side B</title>
<link rel="stylesheet" href="https://fonts.googleapis.com/css2?family=Kaushan+Script&family=Archivo+Black&display=swap">
<style>
  :root {
    --paper: #ffffff;
    --ink: #000000;
    --pattern-grey: #cdd6d9;
    --pattern-grey-deep: #a9b5b8;
    --band-blue-light: #a6dbe8;
    --band-blue: #4bb6d4;
    --band-blue-deep: #2c62a9;
    --band-lime: #c9e13b;
    --band-pink: #f06aa9;
    --band-amber: #f5bd26;
    --swirl-dark: #3d3535;
    --title-green: #9ccf1e;
    --title-edge: #2f4a06;
    --marker-red: #ff0000;
    --marker-blue: #00a0c6;
  }
  html, body {
    margin: 0;
    padding: 0;
    overflow: hidden;
    background: var(--paper);
  }
  .sheet {
    width: 670px;
    height: 1200px;
    position: relative;
    overflow: hidden;
  }
  .sheet svg { display: block; }
  .side-letter {
    font-family: "Archivo Black", sans-serif;
    font-size: 30px;
    fill: var(--ink);
  }
  .label-title {
    font-family: "Kaushan Script", cursive;
    font-size: 31px;
    fill: var(--title-green);
    stroke: var(--title-edge);
    stroke-width: 0.8px;
    paint-order: stroke;
  }
  .spindle-hole { fill: var(--ink); }
  .spindle-ring { fill: none; stroke: var(--paper); stroke-width: 1; }
  .bleed-line-red { stroke: var(--marker-red); stroke-width: 0.6; }
  .bleed-line-blue { stroke: var(--marker-blue); stroke-width: 0.6; }
  .marker-red { fill: var(--marker-red); }
  .marker-blue { fill: var(--marker-blue); }
</style>
</head>
<body>
<main class="sheet">
  <svg width="670" height="1200" viewBox="0 0 670 1200" xmlns="http://www.w3.org/2000/svg">
    <defs>
      <clipPath id="side-a-disc"><circle cx="340" cy="301" r="285"/></clipPath>
      <linearGradient id="blue-band-fill" x1="0.2" y1="0.1" x2="0.9" y2="0.9">
        <stop offset="0" stop-color="var(--band-blue-light)"/>
        <stop offset="0.5" stop-color="var(--band-blue)"/>
        <stop offset="1" stop-color="var(--band-blue-deep)"/>
      </linearGradient>
      <linearGradient id="pattern-fill" x1="0" y1="0" x2="1" y2="1">
        <stop offset="0" stop-color="var(--pattern-grey)"/>
        <stop offset="0.6" stop-color="var(--pattern-grey)"/>
        <stop offset="1" stop-color="var(--pattern-grey-deep)"/>
      </linearGradient>
      <radialGradient id="swirl-fill" cx="0.5" cy="0.5" r="0.5">
        <stop offset="0" stop-color="var(--swirl-dark)" stop-opacity="0.28"/>
        <stop offset="1" stop-color="var(--swirl-dark)" stop-opacity="0"/>
      </radialGradient>
    </defs>

    <!-- Side A -->
    <g class="label-side label-side-a">
      <text class="side-letter" x="64" y="56">A</text>
      <g clip-path="url(#side-a-disc)">
        <rect x="40" y="0" width="600" height="600" fill="url(#pattern-fill)"
              role="img" aria-label="Fine grey chevron pattern with soft blue ink spots"/>
        <polygon class="band band-blue" points="0,29.5 670,699.5 670,548 0,-122" fill="url(#blue-band-fill)"/>
        <polygon class="band band-lime" points="0,-122 670,548 670,433 0,-237" fill="var(--band-lime)"/>
        <polygon class="band band-pink" points="0,-237 670,433 670,320 0,-350" fill="var(--band-pink)"/>
        <polygon class="band band-amber" points="0,-350 670,320 670,-400 0,-400" fill="var(--band-amber)"/>
        <ellipse cx="420" cy="230" rx="240" ry="230" fill="url(#swirl-fill)"
                 role="img" aria-label="Dark floral swirls with leaves, flowers and small rings"/>
      </g>
      <text class="label-title" x="80" y="408" textLength="364" lengthAdjust="spacingAndGlyphs">Minimal and House music</text>
      <circle class="spindle-hole" cx="340" cy="301" r="18.5"/>
      <circle class="spindle-ring" cx="340" cy="301" r="18.5"/>
      <line class="bleed-line-red" x1="557" y1="488" x2="590" y2="520"/>
      <line class="bleed-line-blue" x1="525" y1="520" x2="558" y2="553"/>
      <circle class="marker-red" cx="601" cy="531" r="17.5"/>
      <circle class="marker-blue" cx="568" cy="564" r="17.5"/>
    </g>

    <!-- Side B -->
    <g class="label-side label-side-b">
      <text class="side-letter" x="64" y="628">B</text>
      <circle cx="340" cy="874" r="285" fill="url(#pattern-fill)"
              role="img" aria-label="Fine grey chevron pattern covering the whole label"/>
      <circle class="spindle-hole" cx="340" cy="874" r="18.5"/>
      <line class="bleed-line-red" x1="557" y1="1060" x2="590" y2="1092"/>
      <line class="bleed-line-blue" x1="525" y1="1092" x2="558" y2="1125"/>
      <circle class="marker-red" cx="601" cy="1103" r="17.5"/>
      <circle class="marker-blue" cx="568" cy="1136" r="17.5"/>
    </g>
  </svg>
</main>
</body>
</html>
```